Clear Coat 5L & 2.5L kit

Clear coat 5 Liter with 2.5 Liter hardener
I attached few examples
Required size:
5L
Actual size is: 22.875 x 10.4375 inch
With bleed added: 23.125 x 10.6875 inch
2.5L
Actual size is: 22.875 x 6.1875 inch
With bleed added: 23.125x6.2125 inch

Thanks

```html
<!DOCTYPE html>
<html lang="en">
<head>
<meta charset="utf-8">
<title>Norda Refinish – Ultra Clear Coat 5L label</title>
<link href="https://fonts.googleapis.com/css2?family=Montserrat:wght@400;600;700;800&family=Roboto+Condensed:wght@300;400;700&display=swap" rel="stylesheet">
<style>
  :root{
    --page-top:#f6f8f9;
    --page-bottom:#cfdfe4;
    --label-navy:#0c1420;
    --label-deep:#0a1a28;
    --panel-black:#05070b;
    --brand-yellow:#f7c81b;
    --mint:#5fd0b4;
    --teal-dots:#3f9e97;
    --white:#ffffff;
    --muted:#d9dde2;
  }
  *{box-sizing:border-box;margin:0;padding:0}
  html,body{width:1200px;height:1039px;overflow:hidden}
  body{
    background:linear-gradient(180deg,var(--page-top) 0%,var(--page-top) 20%,var(--page-bottom) 100%);
    font-family:"Roboto Condensed",Arial,sans-serif;
    position:relative;
  }
  .label{
    position:absolute;left:45px;top:217px;width:1112px;height:508px;
    background:linear-gradient(180deg,var(--label-navy) 0%,var(--label-deep) 100%);
    overflow:hidden;
  }
  .wave-texture{
    position:absolute;inset:0;
    background:
      radial-gradient(ellipse 320px 120px at 150px 420px,rgba(63,158,151,.55),transparent 70%),
      radial-gradient(ellipse 260px 150px at 40px 330px,rgba(63,158,151,.35),transparent 70%),
      radial-gradient(ellipse 380px 110px at 640px 380px,rgba(63,158,151,.32),transparent 70%),
      radial-gradient(ellipse 260px 200px at 1060px 360px,rgba(63,158,151,.38),transparent 70%),
      radial-gradient(ellipse 260px 90px at 760px 80px,rgba(63,158,151,.25),transparent 70%);
  }
  .spine-title{
    position:absolute;left:24px;top:51px;
    writing-mode:vertical-rl;transform:rotate(180deg);
    font-family:"Montserrat",sans-serif;font-size:16px;letter-spacing:.3px;line-height:1;
    color:var(--white);font-weight:700;white-space:nowrap;
  }
  .spine-title .light{color:var(--mint);font-weight:400}
  .panel{position:absolute;top:38px;bottom:0;background:var(--panel-black);overflow:hidden}
  .panel-front{left:212px;width:244px}
  .panel-legal{left:540px;width:125px}
  .panel-directions{left:741px;width:258px}

  .brand{font-family:"Montserrat",sans-serif;font-weight:700;color:var(--white);line-height:1}
  .panel-front .brand-name{position:absolute;left:26px;top:40px;font-size:50px;letter-spacing:-1px}
  .panel-front .brand-sub{position:absolute;left:27px;top:100px;font-size:24px;letter-spacing:2.5px}
  .brand-dot{display:inline-block;width:12px;height:12px;border-radius:50%;background:var(--brand-yellow);margin-left:4px;vertical-align:middle}

  .product-line{position:absolute;left:28px;top:170px;font-family:"Montserrat",sans-serif;color:var(--mint);font-size:17px;font-weight:400;line-height:1}
  .product-name{position:absolute;left:25px;top:191px;font-family:"Montserrat",sans-serif;color:var(--white);font-size:30px;font-weight:600;letter-spacing:-.5px;line-height:1}
  .voc{position:absolute;left:29px;top:226px;font-size:14px;color:var(--white);font-weight:700;line-height:1}
  .code{position:absolute;right:26px;top:226px;font-size:14px;color:var(--brand-yellow);letter-spacing:2px;line-height:1}
  .volume-big{position:absolute;left:25px;top:400px;font-family:"Montserrat",sans-serif;font-weight:700;font-size:42px;line-height:1;color:var(--brand-yellow)}
  .features{position:absolute;left:133px;top:355px;list-style:none;color:var(--muted);font-size:15px;font-weight:300;line-height:22.5px}
  .features .mix{color:var(--white);font-weight:700}

  .panel-legal .brand-name{position:absolute;left:13px;top:22px;font-size:27px;letter-spacing:-.5px}
  .panel-legal .brand-sub{position:absolute;left:13px;top:56px;font-size:13px;letter-spacing:1.5px}
  .legal-text{position:absolute;left:12px;top:82px;width:104px;font-size:5px;line-height:6.4px;color:var(--muted)}
  .legal-text p{margin-bottom:8px}
  .legal-text strong{color:var(--white);text-transform:uppercase}
  .company{position:absolute;left:11px;top:385px;font-size:7px;line-height:9px;color:var(--muted)}
  .company strong{color:var(--white)}
  .company .made{margin-top:20px;color:var(--white)}
  .volume-side{position:absolute;left:103px;bottom:26px;writing-mode:vertical-rl;transform:rotate(180deg);
    font-family:"Montserrat",sans-serif;font-weight:700;font-size:16px;line-height:1;color:var(--brand-yellow);white-space:nowrap;letter-spacing:1px}

  .panel-directions .brand-name{position:absolute;right:12px;top:20px;font-size:27px;letter-spacing:-.5px}
  .panel-directions .brand-sub{position:absolute;right:12px;top:55px;font-size:13px;letter-spacing:1.5px}
  .directions{position:absolute;left:10px;top:77px;width:240px;font-size:5.8px;line-height:7.9px;color:var(--muted)}
  .directions p{margin-bottom:5px}
  .directions strong{color:var(--white)}
  .directions .intro{width:150px}
  .speed-table{position:absolute;right:23px;top:75px;border:.5px solid var(--muted);border-collapse:collapse;font-size:5px;line-height:6px;color:var(--muted)}
  .speed-table td{padding:.5px 5px;border-bottom:.5px solid #555}
  .keep-out{font-size:7.5px;line-height:9px;font-weight:700;color:var(--white);margin:4px 0 2px}
  .contents{width:150px}
  .hazard{position:absolute;right:12px;bottom:26px;width:77px;border:.5px solid var(--muted);text-align:center;padding:2px 0 3px;font-size:8px;line-height:9px;font-weight:700;color:var(--white)}
  .hazard svg{display:block;margin:2px auto 0}
</style>
</head>
<body>
<main class="label" aria-label="Norda Refinish Ultra Clear Coat 5 liter label">
  <div class="wave-texture" role="img" aria-label="Flowing teal dotted wave pattern across the dark navy background"></div>

  <div class="spine-title"><span class="light">ULTRA</span> CLEAR COAT</div>

  <section class="panel panel-front">
    <div class="brand brand-name">NORDA<span class="brand-dot"></span></div>
    <div class="brand brand-sub">REFINISH</div>
    <div class="product-line">ULTRA</div>
    <div class="product-name">CLEAR COAT</div>
    <div class="voc">VOC 2.1</div>
    <div class="code">221</div>
    <div class="volume-big">5L</div>
    <ul class="features">
      <li>High Gloss</li>
      <li>Good Leveling</li>
      <li>Easy Application</li>
      <li class="mix">2:1 MIX</li>
    </ul>
  </section>

  <section class="panel panel-legal">
    <div class="brand brand-name">NORDA</div>
    <div class="brand brand-sub">REFINISH</div>
    <div class="legal-text">
      <p><strong>For sale only by professionals.<br>Not for sale to or use by general public</strong></p>
      <p><strong>Notice to purchasers: Limited warranty.</strong> The following is made in lieu of all express or implied rights, warranties and conditions. All goods are manufactured of first class materials. Neither seller nor manufacturer has control over the use and application of the product. It is the responsibility of the purchaser to determine the suitability of the product for its intended use. The liability of the seller and manufacturer shall not exceed the purchase price of the product.</p>
      <p><strong>Warning: flammable liquid and vapor. Vapors and spray mist harmful if inhaled. May cause central nervous system effects such as dizziness, headache or nausea. May cause nose, throat, eye and skin irritation. (Follow all directions and cautions on back panel)</strong></p>
      <p><strong>Warranty:</strong> The recommendations for application of this product are based on data obtained by our own research facilities and is believed accurate. The manufacturer warrants all material sold by it against defects in the material but does not warrant its fitness for any specific application use. The manufacturer makes no other warranty of this material express or implied. This product is intended to be used solely by professionally trained personnel using proper equipment.</p>
    </div>
    <div class="company">
      <strong>Norda Refinish, Inc.</strong><br>
      412 Harbor Point Rd,<br>
      Westfield, CA 90210<br>
      (800) 555-0147
      <div class="made">Made in EU</div>
    </div>
    <div class="volume-side">5 LITERS</div>
  </section>

  <section class="panel panel-directions">
    <div class="brand brand-name">NORDA</div>
    <div class="brand brand-sub">REFINISH</div>
    <table class="speed-table">
      <tr><td>Speed</td><td>Temperature</td></tr>
      <tr><td>Slow</td><td>80°F-100°F</td></tr>
      <tr><td>Medium</td><td>68°F-80°F</td></tr>
      <tr><td>Fast</td><td>50°F-68°F</td></tr>
    </table>
    <div class="directions">
      <p class="intro"><strong>Description:</strong> Hardener for clear coat to be used with ULTRA clear coat. Hardeners are available in three speeds. Please choose the appropriate speed according to weather conditions.</p>
      <p><strong>DIRECTIONS:</strong><br>
      1. Read all label directions, warnings and cautions on paint and catalyst.<br>
      2. Mixing directions for Clear Coat with Activator: 2 Parts Clear / 1 Part Activator.<br>
      3. Adjust air pressure to 50-60 psi at the gun (siphon), 40-45 psi (gravity), 10 psi (HVLP).<br>
      4. Apply 2 full coats, allowing 10-15 minutes flash time between coats. Allow ample flash times.<br>
      5. When force drying, flash for 10-15 minutes, then force dry for 40 minutes at 140°F. Clear may be wet sanded after 2-4 hours. Baking the clear will increase gloss.<br>
      6. Accelerator: Add 2 to 4 oz. to a gallon of catalyzed clear to improve drying times. Note that use of any accelerator will shorten pot life and slightly reduce gloss.<br>
      7. Wet sand with 1500 grit or finer paper after 8 hours. Buff with appropriate compound.<br>
      8. Clean spray equipment immediately after use with lacquer thinner.</p>
      <p><strong>WARNING! FLAMMABLE. VAPOR AND SPRAY MIST HARMFUL. MAY CAUSE LUNG IRRITATION AND ALLERGIC RESPIRATION REACTION.</strong> Keep away from heat, sparks and open flames. Isocyanates can cause lung and skin sensitization and lung damage. Not to be used by persons who have lung or breathing problems or have reaction to isocyanates. Do not inhale vapors. Do not get in eyes, on skin or on clothing. Do not take internally. Use only in well ventilated areas. Wear appropriate, properly fitted approved respirator as directed by the manufacturer. Protect hands with impervious rubber gloves. Wear eye and face protection. Keep container closed when not in use. Empty containers retain product residue and vapor. Dispose of in compliance with federal, state and local regulations. Read the current safety data sheet before opening each container.</p>
      <p><strong>FIRST AID:</strong> In case of headache, dizziness, respiratory irritation or other symptoms of overexposure, move from affected area and avoid further exposure. In case of skin contact, wash skin thoroughly with soap and water. In case of eye contact flush eyes with running water for at least 15 minutes and get medical attention immediately. If ingested, contact physician immediately.</p>
      <p><strong>NOTICE:</strong> Reports have associated repeated and prolonged occupational overexposure to solvents with permanent brain and nervous system damage. Intentional misuse by deliberately concentrating and inhaling this product may be harmful or fatal.</p>
      <p><strong>Proposition 65 Statement: WARNING!</strong> This product contains a chemical known to the state of California to cause cancer, birth defects or other reproductive harm.</p>
      <div class="keep-out">KEEP OUT OF THE REACH OF CHILDREN</div>
      <p><strong>For professional use only by trained and qualified paint personnel using all proper safety equipment and application techniques.</strong></p>
      <p class="contents"><strong>Contents:</strong> Xylene, Acetone, Butyl Acetate, Methoxy Propyl Acetate, Ethyl Benzene.<br>
      <strong>EMERGENCY TELEPHONE NUMBER: SAFELINE 1-800-555-0199</strong><br>
      Sprayable: 2.1 lbs/gal VOC</p>
    </div>
    <div class="hazard">DANGER
      <svg width="64" height="20" viewBox="0 0 64 20" aria-label="Flammable, health hazard and toxic pictograms" role="img">
        <g fill="#fff" stroke="#e3262b" stroke-width="1.6">
          <circle cx="10" cy="10" r="8.5"/><circle cx="32" cy="10" r="8.5"/><circle cx="54" cy="10" r="8.5"/>
        </g>
        <path d="M10 4c2 3 3 5 3 7a3 3 0 0 1-6 0c0-2 1-3 2-4 0 1 1 2 1 2z" fill="#000"/>
        <path d="M32 4l5 9h-10z" fill="#000"/>
        <circle cx="54" cy="9" r="3.5" fill="#000"/><rect x="52" y="12" width="4" height="3" fill="#000"/>
      </svg>
    </div>
  </section>
</main>
</body>
</html>
```